Motor Vault Website - Part of the Brantley Group

A complimentary website is required for the launch of a 'Motor Vault' - a new service launched by industry renowned BRANTLEY. Motor Vault is an industry-first brand that designs and builds unique subterranean car parks for private residential homes in London and the influential counties within the UK. Please see here the direction of a new BRANTLEY Website - we would like Motor Vault to be complimentary and sit alongside BRANTLEY harmoniously - https://www.brantleyhq.example/brantley-nu-staging Brantley have some images, but whilst more professional images are in production - we have also attached pixmoor photos- named clearly as pixmoor. **Attached files include JPEG, .eps of logo and Brantley library images and Pixmoor Library Images - two versions of logo dependent on background colour. - Website needs to be sleek, chic and masculine.- Colour Palette - Grey/ Black/ White - Same visiual journey as Brantley website- Required areas within the sit include - About Us / Our Work / Contact Page

Target Market(s)

Luxury
Men

Number of Pages Required

2 page

Font styles to use
Sans Serif

Colors
e8e8e8
757575
1b1b1b
000000
9d9d9d
cbcbcb
f5f5f5

Requirements
Must have
• Complimentary of this site - https://www.brantleyhq.example/brantley-nu-staging
Should not have
• Colour

```html
<!DOCTYPE html>
<html lang="en">
<head>
<meta charset="utf-8">
<title>Motor Vault — Part of the Brantley Group</title>
<link rel="stylesheet" href="https://fonts.googleapis.com/css2?family=Libre+Baskerville:wght@400;700&family=Work+Sans:wght@400;500;600&display=swap">
<style>
  :root {
    --white: #ffffff;
    --mist: #f5f5f5;
    --light: #e8e8e8;
    --silver: #cbcbcb;
    --grey: #9d9d9d;
    --mid: #757575;
    --charcoal: #1b1b1b;
    --black: #000000;
    --serif: 'Libre Baskerville', Georgia, serif;
    --sans: 'Work Sans', Arial, sans-serif;
  }
  * { margin: 0; padding: 0; box-sizing: border-box; }
  html, body { width: 1200px; height: 3158px; overflow: hidden; }
  body {
    position: relative; background: var(--white); font-family: var(--sans); color: var(--charcoal);
    -webkit-font-smoothing: antialiased; -moz-osx-font-smoothing: grayscale; text-rendering: geometricPrecision;
  }
  .abs { position: absolute; }
  .mono { will-change: transform; transform: translateZ(0); }

  /* Hero */
  .hero { left: 0; top: 0; width: 1200px; height: 674px; }
  .hero-photo { position: absolute; inset: 0; background: radial-gradient(ellipse at 60% 45%, #5a5a5a 0%, #2a2a2a 45%, #0d0d0d 100%); }
  .brand-mark { position: absolute; left: 242px; top: 276px; width: 716px; text-align: center; }
  .brand-name { font-family: var(--sans); font-weight: 500; font-size: 86px; letter-spacing: 4px; color: var(--white); line-height: 1; }
  .brand-tagline { position: absolute; right: 242px; top: 374px; font-family: var(--sans); font-size: 17px; letter-spacing: 1px; color: var(--silver); }

  /* Buttons */
  .btn { position: absolute; height: 38px; font-family: var(--sans); font-weight: 600; font-size: 11px; display: flex; align-items: center; justify-content: center; }
  .btn-dark { background: var(--black); color: var(--white); }
  .btn-light { background: var(--white); color: var(--black); }

  /* Welcome */
  .section-title { position: absolute; left: 0; width: 1200px; text-align: center; font-family: var(--serif); font-size: 28px; font-weight: 400; color: var(--charcoal); }
  .welcome-text { left: 165px; top: 804px; width: 870px; text-align: center; font-size: 12.5px; line-height: 21px; color: var(--mid); }

  /* Split */
  .split-photo { left: 0; top: 1099px; width: 537px; height: 530px; background: linear-gradient(90deg, #2b2b2b 0%, #575757 55%, #bdbdbd 82%, #6a6a6a 100%); }
  .split-panel { left: 537px; top: 1099px; width: 663px; height: 530px; background: var(--black); }
  .split-heading { left: 575px; top: 1196px; width: 480px; font-family: var(--serif); font-weight: 700; font-size: 21px; line-height: 30px; color: var(--white); }
  .split-text { left: 575px; top: 1280px; width: 472px; font-size: 12.5px; line-height: 16.5px; color: var(--white); }

  /* Works */
  .works-title { top: 1705px; font-weight: 700; font-size: 23px; }
  .works-intro { left: 270px; top: 1760px; width: 660px; text-align: center; font-family: var(--serif); font-size: 13.5px; line-height: 19px; color: var(--grey); }
  .works-grid { left: 0; top: 1846px; width: 1200px; height: 362px; display: flex; }
  .work-tile { flex: 1; height: 100%; border-right: 2px solid var(--light); position: relative; }
  .work-tile:last-child { border-right: none; }
  .tile-1 { background: linear-gradient(135deg, #8f8f8f, #5f5f5f 60%, #7c7c7c); }
  .tile-2 { background: linear-gradient(180deg, #6c6c6c, #9a9a9a 60%, #5b5b5b); }
  .tile-3 { background: linear-gradient(160deg, #3a3a3a, #151515 70%); }
  .tile-4 { background: linear-gradient(135deg, #a9a9a9, #cfcfcf 55%, #7e7e7e); }
  .work-label { position: absolute; left: 32px; top: 143px; width: 237px; height: 49px; border: 1px solid var(--mid); display: flex; align-items: center; justify-content: center; font-weight: 600; font-size: 13px; color: var(--white); }
  .work-caption { position: absolute; left: 0; top: 202px; width: 100%; text-align: center; font-size: 13px; line-height: 18px; color: var(--white); }

  /* Contact */
  .contact { left: 0; top: 2208px; width: 1200px; height: 552px; background: linear-gradient(180deg, #2a2a2a 0%, #1f1f1f 50%, #3a3a3a 100%); }
  .contact-title { color: var(--white); top: 2290px; font-weight: 700; font-size: 23px; }
  .contact-intro { left: 250px; top: 2352px; width: 700px; text-align: center; font-family: var(--serif); font-size: 13.5px; line-height: 21px; color: var(--white); }
  .field { position: absolute; width: 202px; }
  .field-label { height: 14px; line-height: 14px; font-weight: 600; font-size: 10px; letter-spacing: 0.5px; color: var(--white); text-transform: uppercase; }
  .field-label sup { font-size: 12px; line-height: 0; }
  .field-input { margin-top: 16px; padding: 0 0 8px 10px; border-bottom: 1px solid var(--light); font-size: 12px; font-style: italic; color: var(--silver); }

  /* Footer */
  .footer { left: 0; top: 2760px; width: 1200px; height: 398px; background: var(--grey); }
  .footer-brand { left: 0; top: 2820px; width: 1200px; text-align: center; font-weight: 600; font-size: 20px; letter-spacing: 1px; color: var(--charcoal); }
  .footer-address { left: 0; top: 2892px; width: 1200px; text-align: center; font-size: 11px; line-height: 27px; letter-spacing: 0.5px; color: var(--charcoal); text-transform: uppercase; }
  .social { left: 493px; top: 2982px; display: flex; gap: 14px; }
  .social span { width: 32px; height: 32px; border-radius: 50%; background: var(--mist); }
  .social span.active { background: var(--mid); }
  .copyright { left: 0; top: 3062px; width: 1200px; text-align: center; font-size: 10.5px; letter-spacing: 0.5px; color: var(--charcoal); text-transform: uppercase; }
</style>
</head>
<body>

<header class="abs hero">
  <div class="hero-photo" role="img" aria-label="Black and white photograph of an underground construction site with a worker and light beams"></div>
  <div class="brand-mark"><div class="brand-name">MOTOR VAULT</div></div>
  <div class="brand-tagline">PART OF THE BRANTLEY GROUP</div>
</header>

<section>
  <h1 class="section-title" style="top:748px">Welcome to Motor Vault</h1>
  <p class="abs mono welcome-text">Nam tincidunt metus purus, et tristique lorem tristique et. Praesent vulputate dictum lorem, id interdum odio lacinia eu. Curabitur pretium ipsum ac pretium blandit. Nulla at vehicula tortor. Curabitur porttitor tempor lorem ac tristique. Pellentesque id massa non orci commodo semper. Nulla facilisi. Proin aliquet luctus massa sit amet sodales. Sed dictum, nisl et cursus ullamcorper, tellus lectus fermentum nisl, eu facilisis magna nibh eget massa. Sed laoreet egestas ligula, et facilisis enim vulputate ut. Morbi sodales ante non ante tincidunt pharetra. Maecenas euismod tellus pretium, dictum felis et, semper leo. Nulla at vehicula tortor. Curabitur porttitor tempor lorem ac tristique. Pellentesque id massa non orci commodo semper.</p>
  <a class="btn btn-dark" style="left:537px;top:964px;width:128px">Learn More</a>
</section>

<section>
  <div class="abs split-photo" role="img" aria-label="Black and white photograph of an empty concrete underground car park"></div>
  <div class="abs split-panel"></div>
  <h2 class="abs split-heading">Nam tincidunt metus purus, et tristique lorem tristique et</h2>
  <p class="abs mono split-text">Nam tincidunt metus purus, et tristique lorem tristique et. Praesent vulputate dictum lorem, id interdum odio lacinia eu. Curabitur pretium ipsum ac pretium blandit. Nulla at vehicula tortor. Curabitur porttitor tempor lorem ac tristique. Pellentesque id massa non orci commodo semper. Nulla facilisi. Proin aliquet luctus massa sit amet sodales. Sed dictum, nisl et cursus ullamcorper, tellus lectus fermentum nisl, eu facilisis magna nibh eget massa. Sed laoreet egestas ligula, et facilisis enim vulputate ut. Morbi sodales ante non ante tincidunt pharetra. Maecenas euismod tellus pretium, dictum felis et, semper leo. Nulla at vehicula tortor. Curabitur porttitor tempor lorem ac tristique. Pellentesque id massa non orci commodo semper.</p>
  <a class="btn btn-light" style="left:575px;top:1516px;width:128px">Learn More</a>
</section>

<section>
  <h2 class="section-title works-title">Our Works</h2>
  <p class="abs mono works-intro">Curabitur eu adipiscing lacus, a iaculis diam. Nullam placerat blandit auctor. Nulla accumsan ipsum et nibh rhoncus, eget tempus sapien ultricies. Donec mollis lorem vehicula.</p>
  <div class="abs works-grid">
    <div class="work-tile tile-1" role="img" aria-label="Close-up photograph of a car wheel rim"></div>
    <div class="work-tile tile-2" role="img" aria-label="Photograph of a long underground corridor with columns"></div>
    <div class="work-tile tile-3" role="img" aria-label="Photograph of steel ceiling structure in a basement">
      <div class="work-label">WORK 1</div>
      <div class="work-caption mono">Morbi sodales ante non<br>ante tincidunt pharetra.</div>
    </div>
    <div class="work-tile tile-4" role="img" aria-label="Photograph of a finished basement with perforated wall panels"></div>
  </div>
</section>

<section>
  <div class="abs contact" role="img" aria-label="Dark photograph of an excavated underground site with ladders"></div>
  <h2 class="section-title contact-title">Get in touch</h2>
  <p class="abs mono contact-intro">Curabitur eu adipiscing lacus, a iaculis diam. Nullam placerat blandit auctor. Nulla accumsan ipsum et nibh rhoncus, eget tempus sapien ultricies. Donec mollis lorem vehicula.</p>
  <div class="field" style="left:162px;top:2444px"><div class="field-label">Name<sup>*</sup></div><div class="field-input">your name</div></div>
  <div class="field" style="left:385px;top:2444px"><div class="field-label">E-mail address<sup>*</sup></div><div class="field-input">email@mail.com</div></div>
  <div class="field" style="left:610px;top:2444px"><div class="field-label">Phone number</div><div class="field-input">+49 123 456 789</div></div>
  <div class="field" style="left:836px;top:2444px"><div class="field-label">Subject<sup>*</sup></div><div class="field-input">subject</div></div>
  <div class="field" style="left:162px;top:2524px;width:876px"><div class="field-label">Message<sup>*</sup></div><div class="field-input">type in your message</div></div>
  <a class="btn btn-light" style="left:911px;top:2617px;width:129px;height:40px">Submit</a>
</section>

<footer>
  <div class="abs footer"></div>
  <div class="abs footer-brand">MOTOR VAULT</div>
  <div class="abs footer-address">27 Harrow Lane, London, W9 4LT<br>Tel: 0207 555 0182</div>
  <div class="abs social"><span class="active"></span><span></span><span></span><span></span><span></span></div>
  <div class="abs copyright">Copyright © Motor Vault 2019. Terms and conditions | Privacy Policy</div>
</footer>

</body>
</html>
```